Corporate Two Sided Business Card

Looking for a Corporate "edgy" Modern look and feel for a business card

We are looking at two options. Dark background with our logo on it, white background with our logo on it - The background is more - Charcoal / Graphite then black

Details will be

Danielle Forsk

Licensee / Director

m. 0428 519 064

e. danielle@quorvela.com.au

quorvela.com.au

Target Market(s)

Professional Business people that refer use business and clients that own Investment Properties

Industry/Entity Type

Business

Contact Information for Business Card

Details will be

Danielle Forsk

Licensee / Director

m. 0428 519 064

quorvela.com.au

Font styles to use
Serif

Colors
000000
ec1f27
eeeeee
ffffff

Requirements
Must have
• Two options - White Background and Dark Background. - Two sided
Nice to have
• A design that is edgy, modern and new to look instead of boring style corporate cards - It should be a full integrated design
Should not have
• Block looking - Cheap.

```html
<!DOCTYPE html>
<html lang="en">
<head>
<meta charset="utf-8">
<title>Quorvela Business Card</title>
<link rel="stylesheet" href="https://fonts.googleapis.com/css2?family=Arimo:wght@400;700&display=swap">
<style>
  :root {
    --stage: #e4e4e6;
    --charcoal: #555557;
    --charcoal-deep: #4a4a4c;
    --paper: #ffffff;
    --paper-soft: #f3f3f3;
    --ink: #1c1c1c;
    --ink-soft: #3a3a3a;
    --red: #e2202a;
    --rule: #9a9a9a;
  }
  * { margin: 0; padding: 0; box-sizing: border-box; }
  html, body {
    width: 1200px; height: 675px; overflow: hidden;
    background: var(--stage);
    font-family: "Arimo", Arial, sans-serif;
  }
  .stage {
    position: relative; width: 1200px; height: 675px;
    display: flex; align-items: center; justify-content: center; gap: 60px;
  }
  .card {
    position: relative; width: 500px; height: 305px; overflow: hidden;
    box-shadow: 0 6px 18px rgba(0,0,0,0.18);
  }
  /* Back side */
  .card-back {
    background: var(--charcoal);
    display: flex; align-items: center; justify-content: center;
  }
  .back-mark {
    display: flex; align-items: center; gap: 12px;
    color: var(--paper); font-weight: 700; font-size: 34px; letter-spacing: 0.5px;
  }
  .back-mark .mark-square { width: 22px; height: 22px; background: var(--paper); }
  /* Front side */
  .card-front {
    background: linear-gradient(160deg, var(--paper) 0%, var(--paper) 55%, var(--paper-soft) 100%);
  }
  .brand {
    position: absolute; left: 34px; top: 52px;
    display: flex; align-items: center; gap: 10px;
    color: var(--ink-soft); font-weight: 700; font-size: 40px; letter-spacing: 0.3px;
  }
  .brand .mark-square { width: 20px; height: 20px; background: var(--red); }
  .contact {
    position: absolute; left: 52px; top: 130px; color: var(--ink);
  }
  .contact .name { font-weight: 700; font-size: 21px; }
  .contact .role { font-size: 13px; margin-top: 2px; color: var(--ink-soft); }
  .contact .divider { width: 108px; height: 1px; background: var(--rule); margin: 10px 0 9px 18px; }
  .contact .line { font-size: 13px; line-height: 17px; margin-left: 18px; color: var(--ink-soft); }
  .footer-bands { position: absolute; left: 0; bottom: 0; width: 500px; height: 70px; }
  .website {
    position: absolute; right: 18px; bottom: 15px;
    color: var(--paper); font-size: 13px; letter-spacing: 0.2px;
  }
</style>
</head>
<body>
<main class="stage">
  <section class="card card-back" aria-label="Card back">
    <div class="back-mark"><span class="mark-square"></span>quorvela</div>
  </section>

  <section class="card card-front" aria-label="Card front">
    <div class="brand"><span class="mark-square"></span>quorvela</div>
    <div class="contact">
      <p class="name">Danielle Forsk</p>
      <p class="role">Licensee / Director</p>
      <div class="divider"></div>
      <p class="line">0428 519 064</p>
      <p class="line">danielle@quorvela.com.au</p>
    </div>
    <svg class="footer-bands" viewBox="0 0 500 70" aria-hidden="true">
      <polygon points="330,16 500,16 500,70 0,70 0,64 315,64" fill="var(--charcoal)"/>
      <polygon points="0,44 318,44 318,24 330,16 330,56 0,56" fill="var(--red)"/>
      <rect x="0" y="56" width="330" height="8" fill="var(--paper)"/>
    </svg>
    <p class="website">quorvela.com.au</p>
  </section>
</main>
</body>
</html>
```